Rollup Banner & Flyer für eine Messe "Erfolg durch Innovation"

Wir benötigten für eine Messe einen Roll Up Banner und Flyer zum verteilen. Gerne basierend auf der aktuellen Firmenpräsentation und mit unseren Referenzen.
Im flyer sollen unserer Leistungen (Datenanalyse, Simulation, Optimierung und Webapplikation) dargestellt werden mit einem kleinen Text und einem aussagekräftigen bild. (https://www.velkador.ch/leistungen/)

Target Market(s)

Industrie

Industry/Entity Type

Simulation

Font styles to use
Sans Serif
Other font styles liked:
• Roboto

Requirements
Must have
• Logo, Referenzen

```html
<!DOCTYPE html>
<html lang="de">
<head>
<meta charset="utf-8">
<title>Velkador – Leistungen Roll-up</title>
<link href="https://fonts.googleapis.com/css2?family=Roboto:wght@300;400;500;700&display=swap" rel="stylesheet">
<style>
  :root {
    --lime: #dbe062;
    --ink: #0b0b0b;
    --paper: #ffffff;
    --stage: #eceeef;
    --muted-dark: #222;
    --muted-light: #d8d8d8;
  }
  * { box-sizing: border-box; margin: 0; padding: 0; }
  html, body { width: 1200px; height: 1200px; overflow: hidden; }
  body {
    background: var(--stage);
    font-family: "Roboto", Arial, sans-serif;
    position: relative;
  }
  .rollup {
    position: absolute;
    left: 400px; top: 62px;
    width: 400px; height: 1076px;
    background: var(--paper);
    overflow: hidden;
  }
  .brand {
    position: absolute; top: 62px; left: 0; width: 100%;
    display: flex; justify-content: center; align-items: center; gap: 12px;
  }
  .brand-dot {
    width: 40px; height: 40px; border-radius: 50%;
    background: var(--lime);
  }
  .brand-name {
    font-size: 44px; font-weight: 500; color: var(--lime);
    letter-spacing: 1px;
  }
  .product-visual {
    position: absolute; left: 96px; top: 152px;
    width: 190px; height: 200px;
    background: linear-gradient(180deg, #dfe2e6 0%, #b9c3cf 55%, #e9eaec 100%);
    border-radius: 4px;
  }
  .headline {
    position: absolute; top: 358px; left: 0; width: 100%;
    text-align: center; font-size: 58px; font-weight: 700; color: var(--ink);
    letter-spacing: -0.5px;
  }
  .intro {
    position: absolute; top: 440px; left: 50px; width: 300px;
    text-align: center; font-size: 8px; line-height: 1.35; font-weight: 400; color: var(--muted-dark);
  }
  .intro p + p { margin-top: 7px; }
  .services {
    position: absolute; top: 537px; left: 0; width: 100%; height: 539px;
    background: var(--ink);
  }
  .service { position: absolute; left: 0; width: 100%; }
  .service-icon {
    position: absolute; left: 30px; top: 18px; width: 50px; height: 50px;
  }
  .service-title {
    position: absolute; left: 116px; top: 0;
    font-size: 24px; font-weight: 500; color: var(--lime);
  }
  .service-text {
    position: absolute; left: 116px; top: 36px; width: 252px;
    font-size: 8px; line-height: 1.35; font-weight: 300; color: var(--muted-light);
  }
  .wave { position: absolute; left: 0; bottom: 0; width: 400px; height: 70px; display: block; }
  .service-icon * { fill: none; stroke: var(--lime); stroke-width: 2; stroke-linecap: round; stroke-linejoin: round; }
</style>
</head>
<body>
<main class="rollup">
  <header class="brand">
    <span class="brand-dot"></span>
    <span class="brand-name">Velkador</span>
  </header>

  <div class="product-visual" role="img" aria-label="Bildschirm mit 3D-Simulation einer Lagerhalle"></div>

  <h1 class="headline">Leistungen</h1>

  <div class="intro">
    <p>Mit Simulation, Datenanalyse und Optimierung entwickeln wir Lösungen, die komplexe Prozesse sichtbar machen, Varianten vergleichbar machen und bessere Entscheidungen ermöglichen.</p>
    <p>Wir begleiten unsere Kunden vom schnellen Vorprojekt bis zur produktiven Lösung – pragmatisch, technisch stark und immer mit Fokus auf dem Nutzen.</p>
  </div>

  <section class="services">
    <article class="service" style="top:34px">
      <svg class="service-icon" viewBox="0 0 50 50" aria-hidden="true">
        <ellipse cx="25" cy="25" rx="22" ry="9" transform="rotate(35 25 25)"/>
        <ellipse cx="25" cy="25" rx="22" ry="9" transform="rotate(-35 25 25)"/>
        <ellipse cx="25" cy="19" rx="7" ry="3"/>
        <path d="M18 19v12c0 1.7 3.1 3 7 3s7-1.3 7-3V19M18 25c0 1.7 3.1 3 7 3s7-1.3 7-3"/>
      </svg>
      <h2 class="service-title">Datenanalyse</h2>
      <p class="service-text">Datenanalyse macht Prozesse sichtbar, erkennt Muster und schafft eine objektive Grundlage für Entscheidungen. Wir strukturieren, bereinigen und analysieren Daten so, dass sie einen echten Nutzen erzeugen.</p>
    </article>

    <article class="service" style="top:163px">
      <svg class="service-icon" viewBox="0 0 50 50" aria-hidden="true">
        <rect x="4" y="8" width="42" height="30" rx="2"/>
        <path d="M20 44h10M25 38v6M9 18h4l2-5 3 9 2-4h4"/>
        <rect x="9" y="27" width="6" height="6"/>
        <rect x="18" y="27" width="6" height="6"/>
        <path d="M30 14h11M30 20h11M30 26h11M30 32h11"/>
      </svg>
      <h2 class="service-title">Simulation</h2>
      <p class="service-text">Simulation bildet reale Prozesse digital ab, damit Abläufe, Kapazitäten und Varianten risikofrei getestet werden können.</p>
    </article>

    <article class="service" style="top:272px">
      <svg class="service-icon" viewBox="0 0 50 50" aria-hidden="true">
        <rect x="17" y="3" width="16" height="18" rx="1"/>
        <path d="M21 9h8M21 13h8M21 17h5M25 21v6M8 14v13h34V14M8 14h9M42 14h-9"/>
        <circle cx="25" cy="34" r="6"/>
        <circle cx="25" cy="34" r="2"/>
        <path d="M8 27v13M42 27v13M25 40v6"/>
        <circle cx="8" cy="42" r="2"/><circle cx="42" cy="42" r="2"/>
      </svg>
      <h2 class="service-title">Optimierung</h2>
      <p class="service-text">Optimierung sucht automatisch nach der besten Lösung – sei es bei Planung, Ressourcen, Routen oder Abläufen. Mit Algorithmen und intelligenten Modellen finden wir Varianten, die Kosten senken, Kapazitäten besser nutzen und Entscheidungen beschleunigen.</p>
    </article>

    <article class="service" style="top:394px">
      <svg class="service-icon" viewBox="0 0 50 50" aria-hidden="true">
        <rect x="4" y="8" width="42" height="30" rx="2"/>
        <path d="M20 44h10M25 38v6M4 14h42"/>
        <rect x="10" y="19" width="20" height="12"/>
        <path d="M14 25h12M33 28l7 3-3 1-1 3z"/>
      </svg>
      <h2 class="service-title">Webapplikationen</h2>
      <p class="service-text">Wir entwickeln individuelle Webapplikationen, die Daten, Simulationen und Optimierungen in einem benutzerfreundlichen Tool zusammenführen. So entstehen Lösungen, die direkt im Alltag genutzt werden – einfach, schnell und ohne Installation.</p>
    </article>

    <svg class="wave" viewBox="0 0 400 70" preserveAspectRatio="none" aria-hidden="true">
      <path d="M0 18 C 90 0, 170 48, 270 30 C 330 20, 370 8, 400 14 L400 70 L0 70 Z" fill="var(--lime)"/>
    </svg>
  </section>
</main>
</body>
</html>
```